Process Flow Chart for Real Estate Agency

We need a visual flow chart of the process of selling a home for our Real Estate Agency. This visual will be provided to all new staff to explain the process and also to potential clients to explain how detailed the process is. It needs to show each step as detailed in the attached word doc and use icons and arrows to show the direction of flow.

Target Market(s)

Staff & Potential Clients

Industry/Entity Type

Real Estate

Font styles to use
Sans Serif

Colors

Designer to choose colors to be used in the design.

Requirements
Must have
• Easy to read, lots of icons, colour coded with Agent in one colour, Admin in another (some tasks are either/or so not sure what to colour those ones.)
Nice to have
• Include one of the two attached logos

```html
<!DOCTYPE html>
<html lang="en">
<head>
<meta charset="utf-8">
<title>Tasks Flow Chart – HarbourLane Real Estate</title>
<link href="https://fonts.googleapis.com/css2?family=Open+Sans:wght@400;600;700&family=Russo+One&display=swap" rel="stylesheet">
<style>
  :root{
    --stage:#e6e9ec;
    --sheet:#ffffff;
    --panel:#2b8fd6;
    --agent:#2b8fd6;
    --admin:#f39019;
    --divider:#d7dde3;
    --ink:#2b8fd6;
  }
  *{box-sizing:border-box;margin:0;padding:0}
  html,body{width:1200px;height:675px;overflow:hidden;background:var(--stage);font-family:"Open Sans",Arial,sans-serif}
  .sheet{position:absolute;left:30px;top:22px;width:1140px;height:631px;background:var(--sheet);box-shadow:0 6px 18px rgba(0,0,0,.12)}
  .brand{position:absolute;left:34px;top:48px;display:flex;align-items:center;gap:10px}
  .brand-dot{width:30px;height:30px;border-radius:50%;background:var(--admin)}
  .brand-name{font-weight:700;font-size:24px;color:var(--agent);letter-spacing:-.3px}
  .chart-title{position:absolute;right:40px;top:38px;font-family:"Russo One",Arial,sans-serif;font-size:34px;letter-spacing:3px;color:var(--ink);font-style:italic}
  .flow-panel{position:absolute;left:26px;right:26px;top:128px;bottom:22px;background:var(--panel)}
  .step{position:absolute;width:300px;height:86px;background:#fff;border-radius:14px;display:flex;align-items:center;box-shadow:0 2px 5px rgba(0,0,0,.15)}
  .step-icon{width:72px;height:56px;border-right:1.5px solid var(--divider);display:flex;align-items:center;justify-content:center;flex-shrink:0}
  .step-icon svg{width:40px;height:40px}
  .step-text{padding:0 48px 0 14px;font-size:12px;line-height:1.2;font-weight:600}
  .step-num{position:absolute;top:-13px;right:14px;width:30px;height:30px;border-radius:50%;color:#fff;font-size:13px;font-weight:700;display:flex;align-items:center;justify-content:center;border:2px solid #fff}
  .agent .step-text{color:var(--agent)} .agent .step-num{background:var(--agent)} .agent .step-icon{color:var(--agent)}
  .admin .step-text{color:var(--admin)} .admin .step-num{background:var(--admin)} .admin .step-icon{color:var(--admin)}
  .arrow{position:absolute;width:22px;height:22px;border-radius:50%;background:#fff;display:flex;align-items:center;justify-content:center}
  .arrow svg{width:12px;height:12px;fill:none;stroke:var(--agent);stroke-width:2.6;stroke-linecap:round;stroke-linejoin:round}
</style>
</head>
<body>
<main class="sheet">
  <div class="brand"><span class="brand-dot"></span><span class="brand-name">HarbourLane Real Estate</span></div>
  <h1 class="chart-title">TASKS FLOW CHART</h1>
  <section class="flow-panel"></section>

  <!-- Row 1 -->
  <div class="step agent" style="left:66px;top:152px"><div class="step-icon"><svg viewBox="0 0 40 40" fill="none" stroke="currentColor" stroke-width="3"><path d="M8 24v-4a12 12 0 0 1 24 0v4"/><rect x="5" y="22" width="7" height="10" rx="2" fill="currentColor"/><rect x="28" y="22" width="7" height="10" rx="2" fill="currentColor"/><path d="M31 32q0 4-8 4"/></svg></div><p class="step-text">Agent calls potential client to arrange a time to meet and obtain details about the property</p><span class="step-num">01</span></div>
  <div class="step agent" style="left:426px;top:152px"><div class="step-icon"><svg viewBox="0 0 40 40" fill="none" stroke="currentColor" stroke-width="3"><rect x="6" y="8" width="26" height="26" rx="2"/><path d="M12 20l6 6 16-18" stroke-width="4"/></svg></div><p class="step-text">Agent ensures all decision makers will be present at meeting</p><span class="step-num">02</span></div>
  <div class="step agent" style="left:786px;top:106px"><div class="step-icon"><svg viewBox="0 0 40 40" fill="none" stroke="currentColor" stroke-width="3"><rect x="11" y="4" width="18" height="32" rx="3"/><path d="M20 16v8M16 20h8"/><circle cx="20" cy="31" r="1.3" fill="currentColor"/></svg></div><p class="step-text">Agent adds vendors contact details on phone</p><span class="step-num">03</span></div>

  <!-- Row 2 -->
  <div class="step admin" style="left:66px;top:270px"><div class="step-icon"><svg viewBox="0 0 40 40" fill="currentColor"><path d="M4 8h6l5 18h18l4-13H12" fill="none" stroke="currentColor" stroke-width="3"/><circle cx="17" cy="32" r="3"/><circle cx="30" cy="32" r="3"/></svg></div><p class="step-text">Agent/Admin orders ARE from Fairweather's</p><span class="step-num">06</span></div>
  <div class="step admin" style="left:426px;top:270px"><div class="step-icon"><svg viewBox="0 0 40 40" fill="none" stroke="currentColor" stroke-width="3"><rect x="11" y="4" width="18" height="32" rx="3"/><rect x="14" y="14" width="12" height="8" rx="1" fill="currentColor"/></svg></div><p class="step-text">Agent sends SMS to potential client to thank them for the opportunity</p><span class="step-num">05</span></div>
  <div class="step admin" style="left:786px;top:270px"><div class="step-icon"><svg viewBox="0 0 40 40" fill="currentColor"><rect x="5" y="9" width="30" height="26" rx="3"/><rect x="11" y="4" width="3" height="8"/><rect x="26" y="4" width="3" height="8"/><g fill="#fff"><rect x="9" y="17" width="5" height="4"/><rect x="17.5" y="17" width="5" height="4"/><rect x="26" y="17" width="5" height="4"/><rect x="9" y="25" width="5" height="4"/><rect x="17.5" y="25" width="5" height="4"/><rect x="26" y="25" width="5" height="4"/></g></svg></div><p class="step-text">Agent adds appointment to personal calendar</p><span class="step-num">04</span></div>

  <!-- Row 3 -->
  <div class="step agent" style="left:66px;top:388px"><div class="step-icon"><svg viewBox="0 0 40 40" fill="none" stroke="currentColor" stroke-width="3"><rect x="7" y="7" width="22" height="29" rx="2"/><rect x="13" y="4" width="10" height="6" rx="1" fill="currentColor"/><path d="M12 17h12M12 23h12M12 29h6"/><circle cx="30" cy="31" r="6" fill="currentColor"/><path d="M27 31l2 2 4-4" stroke="#fff" stroke-width="2"/></svg></div><p class="step-text">Agent completes a TMP to provide to Admin for Prelisting kit prep</p><span class="step-num">07</span></div>
  <div class="step agent" style="left:426px;top:388px"><div class="step-icon"><svg viewBox="0 0 40 40" fill="none" stroke="currentColor" stroke-width="3"><path d="M5 9l10-3 10 3 10-3v25l-10 3-10-3-10 3z"/><path d="M15 6v25M25 9v25"/></svg></div><p class="step-text">Admin prepares pre-listing kit with questionnaire, sample brochure &amp; cover letter, property magazine, agent profile booklet</p><span class="step-num">08</span></div>
  <div class="step agent" style="left:786px;top:388px"><div class="step-icon"><svg viewBox="0 0 40 40" fill="none" stroke="currentColor" stroke-width="3"><rect x="8" y="4" width="18" height="32"/><circle cx="22" cy="21" r="1.5" fill="currentColor"/><path d="M30 14v12l5-6z" fill="currentColor"/></svg></div><p class="step-text">Admin/Agent delivers pre-listing kit (preferably within the hour) &amp; SMS potential vendor</p><span class="step-num">09</span></div>

  <!-- Row 4 -->
  <div class="step admin" style="left:66px;top:506px"><div class="step-icon"><svg viewBox="0 0 40 40" fill="none" stroke="currentColor" stroke-width="3"><circle cx="12" cy="8" r="3"/><path d="M12 11v6h16v8H10v8h14"/><path d="M29 26a5 5 0 1 1 0 .1z" fill="currentColor"/><path d="M29 31v5"/></svg></div><p class="step-text">Admin enters potential Vendor into CRM &amp; set "Appraisal" Track</p><span class="step-num">12</span></div>
  <div class="step admin" style="left:426px;top:506px"><div class="step-icon"><svg viewBox="0 0 40 40" fill="currentColor"><path d="M8 4h18l7 7v25H8z"/><g fill="#fff"><rect x="13" y="15" width="15" height="2.5"/><rect x="13" y="21" width="15" height="2.5"/><rect x="13" y="27" width="10" height="2.5"/></g></svg></div><p class="step-text">Admin prepares TMP with Marketing Costs Selection booklet, Service Offering Selection booklet, Sales Agency Agreement &amp; Benefits Form.</p><span class="step-num">11</span></div>
  <div class="step admin" style="left:786px;top:506px"><div class="step-icon"><svg viewBox="0 0 40 40" fill="none" stroke="currentColor" stroke-width="3"><path d="M8 4h16l7 7v25H8z"/><circle cx="19" cy="20" r="6"/><path d="M23 24l6 6"/></svg></div><p class="step-text">Admin/Agent to research &amp; prints comparable Sales reports</p><span class="step-num">10</span></div>

  <!-- Arrows -->
  <span class="arrow" style="left:390px;top:184px"><svg viewBox="0 0 12 12"><path d="M2 6h8M6 2l4 4-4 4"/></svg></span>
  <span class="arrow" style="left:750px;top:184px"><svg viewBox="0 0 12 12"><path d="M2 6h8M6 2l4 4-4 4"/></svg></span>
  <span class="arrow" style="left:925px;top:242px"><svg viewBox="0 0 12 12"><path d="M6 2v8M2 6l4 4 4-4"/></svg></span>
  <span class="arrow" style="left:750px;top:302px"><svg viewBox="0 0 12 12"><path d="M10 6H2M6 2L2 6l4 4"/></svg></span>
  <span class="arrow" style="left:390px;top:302px"><svg viewBox="0 0 12 12"><path d="M10 6H2M6 2L2 6l4 4"/></svg></span>
  <span class="arrow" style="left:205px;top:361px"><svg viewBox="0 0 12 12"><path d="M6 2v8M2 6l4 4 4-4"/></svg></span>
  <span class="arrow" style="left:390px;top:420px"><svg viewBox="0 0 12 12"><path d="M2 6h8M6 2l4 4-4 4"/></svg></span>
  <span class="arrow" style="left:750px;top:420px"><svg viewBox="0 0 12 12"><path d="M2 6h8M6 2l4 4-4 4"/></svg></span>
  <span class="arrow" style="left:925px;top:479px"><svg viewBox="0 0 12 12"><path d="M6 2v8M2 6l4 4 4-4"/></svg></span>
  <span class="arrow" style="left:750px;top:538px"><svg viewBox="0 0 12 12"><path d="M10 6H2M6 2L2 6l4 4"/></svg></span>
  <span class="arrow" style="left:390px;top:538px"><svg viewBox="0 0 12 12"><path d="M10 6H2M6 2L2 6l4 4"/></svg></span>
</main>
</body>
</html>
```